Elegant and modern body scrub for organic junkies

I need a package design for my new company based out of Austin, Texas. We are focused on cruelty free and all natural and organic products. Our deign needs to be able to have the information we require on it, while still appearing very clean and captivating. Our initial product is a clear skin body scrub, intended for people with problematic skin. Our target market is women and we want to show elegance, without appearing "high end."
Updates

Reason: I want to allot more time for certain designers to submit edits. Last minute proposals have been appealing

Target Market(s)

Women. Organic and holistic minded. Natural beauty lovers.

Industry/Entity Type

Skin Care Product

Font styles to use
Script
Other font styles liked:
• AmericanTypewriter, Beautifulflaws, courier, caviarDreams-bold

Colors
000000
ffc214
ffffff
fece3e
fbee3e

Requirements
Must have
• Must be designed in Adobe Illustrator.
• The photo titled “structure for oz and grams” -That needs to be included at the bottom of 1B. I like the horizontal and vertical bar that separate the two. I want that.
• Color Inspiration - The photo titled “venra color inspiration” and “color combo inspiration” are the colors I want. BLACK, GOLD, WHITE. I want the label background black and the writing in white with some gold somewhere on it. My logo is going to be a golden elephant.
• The photos titled “I like how clean this looks” and “I also like how clean this looks” - I want 1B to look super clean. I don’t want a lot of information in this box. I want simple and clean. This is where the logo and brand name will go.
• Logo - A golden elephant. I want it to be gold and geometric. There can be dimension like this elephant example on the left of the 1B description. I want the trunk to be facing to the left and the trunk needs to be raised overhead and touching the animal's forehead.
• The photo titled “sideways writing and silver rim” - I want 1C to be written sideways like this. My text will be much more extensive so the font won’t be able to be so big.
Nice to have
• The photo titled “sideways writing and silver rim” - I want 1C to be written sideways like this. My text will be much more extensive so the font won’t be able to be so big. I also REALLY like how this label is rimmed in silver, but I would want gold. This is not mandatory, but I really like this.
• The photo titled “melted honey” - This is another option I really like. The gold that looks like honey dripping on the label is really cool. Not mandatory, but I really liked that. I also like the craft background on this.
• Color Inspiration - The photo titled “color inspiration” and “another color inspiration” is an option I would also like to see. Rather than black, I’d like to see what it would ALSO look like with a navy background. NAVY, GOLD, WHITE, maybe black somewhere.
Should not have
• Colorful patterns or excessive info in section 1B.

```html
<!DOCTYPE html>
<html lang="en">
<head>
<meta charset="utf-8">
<title>Clean Skin Body Polish – Label</title>
<link rel="stylesheet" href="https://fonts.googleapis.com/css2?family=Pathway+Gothic+One&family=Montserrat:wght@400&display=swap">
<style>
  :root {
    --backdrop: #e8e6e2;
    --label-paper: #f6f5f2;
    --ink: #1a1a1a;
    --gold: #c9a13a;
    --rule: #2a2a2a;
  }
  html, body {
    margin: 0;
    padding: 0;
    width: 1200px;
    height: 1080px;
    overflow: hidden;
    background: var(--backdrop);
  }
  .canvas {
    position: relative;
    width: 1200px;
    height: 1080px;
  }
  .label {
    position: absolute;
    left: 50px;
    top: 290px;
    width: 1100px;
    height: 500px;
    background: var(--label-paper);
    box-shadow: 0 2px 10px rgba(0,0,0,0.06);
  }
  .brand-mark {
    position: absolute;
    left: 22px;
    top: 100px;
    width: 305px;
    height: 294px;
    display: flex;
    align-items: center;
    justify-content: center;
    font-family: "Pathway Gothic One", sans-serif;
    font-size: 110px;
    color: var(--gold);
    letter-spacing: 4px;
  }
  .product-title {
    position: absolute;
    left: 443px;
    margin: 0;
    font-family: "Pathway Gothic One", sans-serif;
    font-weight: 400;
    color: var(--ink);
    line-height: 1;
    white-space: nowrap;
  }
  .title-clean  { top: 50px;  font-size: 150px; letter-spacing: 3px; }
  .title-skin   { top: 191px; font-size: 97px;  letter-spacing: 0; }
  .title-polish { top: 279px; font-size: 146px; letter-spacing: 0; }
  .rules {
    position: absolute;
    left: 0;
    top: 0;
    width: 1100px;
    height: 500px;
  }
  .rules line {
    stroke: var(--rule);
    stroke-width: 2.5;
  }
  .net-weight {
    position: absolute;
    top: 446px;
    font-family: "Montserrat", sans-serif;
    font-size: 26px;
    color: var(--ink);
  }
  .weight-oz { left: 469px; }
  .weight-gr { left: 621px; }
  .brand-name {
    position: absolute;
    left: 822px;
    top: 268px;
    transform: translate(-50%, -50%) rotate(-90deg);
    font-family: "Montserrat", sans-serif;
    font-size: 36px;
    letter-spacing: 9px;
    color: var(--ink);
    white-space: nowrap;
  }
</style>
</head>
<body>
<main class="canvas">
  <section class="label">
    <div class="brand-mark">venra</div>

    <h1 class="product-title title-clean">CLEAN</h1>
    <p class="product-title title-skin">SKIN BODY</p>
    <p class="product-title title-polish">POLISH</p>

    <svg class="rules" viewBox="0 0 1100 500" aria-hidden="true">
      <line x1="443" y1="430" x2="759" y2="430"/>
      <line x1="600" y1="430" x2="600" y2="490"/>
      <line x1="759" y1="50" x2="759" y2="490"/>
    </svg>

    <span class="net-weight weight-oz">12oz</span>
    <span class="net-weight weight-gr">340gr</span>

    <div class="brand-name">BRAND NAME</div>
  </section>
</main>
</body>
</html>
```